broucher for electrical contracting buisness

use website template and attached files for colour scheme / ideas

Industry/Entity Type

Electrical

Requirements
Must have
• A5 folded to A4 4 pp format
• use the written content in the broucher word document as a guide

```html
<!DOCTYPE html>
<html lang="en">
<head>
<meta charset="utf-8">
<title>Brightwell Electrical – Brochure Spread</title>
<link rel="stylesheet" href="https://fonts.googleapis.com/css2?family=Anton&family=Open+Sans:wdth,wght@75..100,300..800&display=swap">
<style>
  :root {
    --navy: #1c2157;
    --navy-deep: #141845;
    --red: #e1383c;
    --paper-left: #e4e4e4;
    --paper-right: #dedede;
    --ink: #4a4a4a;
    --ink-soft: #5c5c5c;
    --box: #ececec;
    --bg: #b9b9b9;
  }
  * { margin: 0; padding: 0; box-sizing: border-box; }
  html, body { width: 1200px; height: 857px; overflow: hidden; background: var(--bg); }
  body { font-family: "Open Sans", Arial, sans-serif; font-stretch: 80%; color: var(--ink); }
  .spread { position: relative; width: 1200px; height: 857px; display: flex; }
  .page { position: relative; width: 600px; height: 857px; overflow: hidden; }
  .page--inside { background: var(--paper-left); }
  .page--cover { background: var(--paper-right); }

  .intro { position: absolute; left: 48px; top: 64px; width: 510px; font-size: 15px; line-height: 1.5; font-weight: 400; color: var(--ink-soft); }
  .price-list { position: absolute; left: 48px; top: 158px; list-style: none; font-size: 14.5px; line-height: 1.55; color: var(--red); }

  .photo { position: absolute; }
  .photo--testing { left: 48px; top: 362px; width: 268px; height: 172px; background: linear-gradient(135deg, #8b8f95 0%, #c9cbcf 45%, #e7d870 60%, #6f737a 100%); }
  .bolt { position: absolute; left: 262px; top: 334px; width: 46px; height: 78px; }

  .service-title { position: absolute; left: 338px; top: 348px; font-size: 25px; font-weight: 800; letter-spacing: 3px; color: var(--red); font-stretch: 100%; }
  .service-body { position: absolute; left: 338px; top: 387px; width: 225px; font-size: 15px; line-height: 1.5; color: var(--ink-soft); }

  .price-callout { position: absolute; left: 348px; top: 538px; font-size: 15px; line-height: 1.3; color: var(--ink-soft); }
  .price-callout strong { display: block; font-size: 31px; font-weight: 400; color: var(--red); margin-top: 2px; }

  .bar-list { position: absolute; list-style: none; font-size: 14.5px; line-height: 1; color: var(--ink); }
  .bar-list li { display: flex; align-items: center; gap: 10px; height: 19px; }
  .bar-list li::before { content: ""; width: 32px; height: 7px; background: var(--navy); }
  .bar-list li:nth-child(even)::before { background: var(--red); }
  .bar-list--tests { left: 48px; top: 552px; }
  .bar-list--promises { left: 20px; top: 470px; }

  .address-panel { position: absolute; left: 130px; top: 665px; width: 430px; height: 160px; border: 2px dashed #444; padding: 12px 16px 14px; }
  .address-panel h3 { font-size: 23px; font-weight: 800; text-align: center; color: #222; font-stretch: 85%; letter-spacing: 0.5px; }
  .address-panel .address-field { margin-top: 8px; height: 96px; background: var(--box); }

  .cover-art { position: absolute; left: 0; top: 0; width: 600px; height: 450px; }
  .cover-headline { font-family: "Anton", Impact, sans-serif; fill: var(--navy-deep); }

  .brand { position: absolute; left: 330px; top: 490px; width: 240px; text-align: center; color: var(--navy); }
  .brand-mark { width: 46px; height: 46px; border-radius: 50%; background: var(--red); margin: 0 auto 10px; }
  .brand-name { font-size: 25px; font-weight: 800; letter-spacing: 1px; line-height: 1; font-stretch: 100%; }
  .brand-licence { font-size: 11px; font-weight: 400; letter-spacing: 2px; margin-top: 4px; }
</style>
</head>
<body>
<main class="spread">

  <section class="page page--inside">
    <p class="intro">Need us to supply and fit? See our following price guide for supply and installation of split system air conditioning to your home or office. (supply and fit prices are quoted as back to back installations only additional costs may apply for installations that differ).</p>

    <ul class="price-list">
      <li>Kaori 1.7/2.0kW Split Air Conditioner supply and fit $1272 (price is GST inclusive)</li>
      <li>Kaori 2.0/2.5kW Split Air Conditioner supply and fit $1402 (price is GST inclusive)</li>
      <li>Kaori 3.5/4kW Split Air Conditioner supply and fit $1506 (price is GST inclusive)</li>
      <li>Kaori 5/5.8kW Split Air Conditioner supply and fit $1999 (price is GST inclusive)</li>
      <li>Kaori 6.3/7.1kW Split Air Conditioner supply and fit $2304 (price is GST inclusive)</li>
      <li>Kaori 8.0/9.0kW Split Air Conditioner supply and fit $2870 (price is GST inclusive)</li>
      <li>Kaori 9.2/10kw Reverse Split Air Conditioner supply and fit $3480 (price is GST inclusive)</li>
    </ul>

    <div class="photo photo--testing" role="img" aria-label="Photo of hands attaching a yellow test tag to an appliance lead beside a testing unit"></div>
    <svg class="bolt" viewBox="0 0 46 78" aria-hidden="true">
      <polygon points="14,0 40,0 28,28 44,28 8,78 20,38 4,38" fill="var(--red)"/>
    </svg>

    <h2 class="service-title">TEST TAG</h2>
    <p class="service-body">Electrical testing and tagging is the process of determining if an electrical item is faulty. Our qualified electrician will visually inspect the item then perform a series of tests including;</p>

    <p class="price-callout">Our test tag<br>prices starts from<strong>$5.50 per item</strong></p>

    <ul class="bar-list bar-list--tests">
      <li>Insulation resistance</li>
      <li>Earth Circuit test</li>
      <li>Earth Leakage Tests</li>
      <li>Polarity</li>
      <li>RCD (Safety Switch) Test</li>
    </ul>

    <div class="address-panel">
      <h3>ADDRESS</h3>
      <div class="address-field"></div>
    </div>
  </section>

  <section class="page page--cover">
    <svg class="cover-art" viewBox="0 0 600 450" aria-label="Services: residential, test tag, industrial, commercial, airconditioning">
      <rect x="0" y="0" width="600" height="205" fill="var(--navy)"/>
      <text class="cover-headline" x="18" y="74" font-size="52">RESIDENTIAL<tspan font-size="36">TEST TAG</tspan></text>
      <text class="cover-headline" x="18" y="128" font-size="50">INDUSTRIAL<tspan font-size="36">COMMERCIAL</tspan></text>
      <text class="cover-headline" x="18" y="176" font-size="44">AIRCONDITIONING</text>
      <polygon points="0,200 420,182 600,150 600,172 0,222" fill="var(--red)"/>
      <polygon points="0,222 600,172 600,392 0,420" fill="#b89a6e" role="img" aria-label="Photo of a warmly lit open-plan living room and kitchen with pendant lights"/>
      <polygon points="210,432 600,372 600,392 230,446" fill="var(--red)"/>
      <polygon points="0,420 600,392 600,450 0,450" fill="var(--paper-right)"/>
      <polygon points="230,446 600,392 600,406 258,450" fill="var(--red)"/>
    </svg>

    <ul class="bar-list bar-list--promises">
      <li>24/7 call outs</li>
      <li>Quality guarantee on all works</li>
      <li>Manufacturer's warranty on all products</li>
      <li>Locally owned and run business</li>
    </ul>

    <div class="brand">
      <div class="brand-mark"></div>
      <div class="brand-name">BRIGHTWELL ELECTRICAL</div>
      <div class="brand-licence">EC 24510</div>
    </div>
  </section>

</main>
</body>
</html>
```